Brindel Clear Springs needs a new business card design (we produce and sell pure bottled water)

We need a clean modern design for our new business cards, We have an existing logo which ultimately cannot be changed, however it could be slighty improved and the colours adjusted. We have this existing logo on all of our bottles, vehicles etc.

Our company slogan is "Clear from the very first sip".
Along with our relevant company information
(Address, phone, website email etc) we will only be using names and not putting position titles for flexibilty.

We are looking for a clean, minimalist modern design.

You can view our website (if need of an update also!) to see our business.

Industry/Entity Type

Business

Contact Information for Business Card

Staff Name : XXXXXX XXXXXX
Address : 8/41 Tallowood St
Marwick Flats QLD 4172
Staff Mobile Number : 04XX XXX XXX
Office Phone Number : 07 3918 4520
Staff Email Address : XXXX@brindelclearsprings.com.au
Website : www.brindelclearsprings.com.au

Font styles to use
Sans Serif

Colors
cee9f5
33a6d7
0492cd
0455a3
3276b5
85abd2
cedeed

Requirements
Must have
• The ability to edit and change the staff members details as we will need to edit for each respective staff member (7 in total)

```html
<!DOCTYPE html>
<html lang="en">
<head>
<meta charset="utf-8">
<title>Brindel Clear Springs – Business Card</title>
<link rel="stylesheet" href="https://fonts.googleapis.com/css2?family=Open+Sans:wght@400;700&family=PT+Serif:ital@0;1&display=swap">
<style>
  :root {
    --page-bg: #eceef1;
    --card-bg: #ffffff;
    --brand-blue: #3b3fae;
    --text-dark: #1f1f24;
    --card-shadow: rgba(20, 24, 40, 0.16);
  }
  * { box-sizing: border-box; margin: 0; padding: 0; }
  html, body {
    width: 1200px;
    height: 1200px;
    overflow: hidden;
    background: var(--page-bg);
  }
  .sheet {
    position: relative;
    width: 1200px;
    height: 1200px;
  }
  .card {
    position: absolute;
    left: 180px;
    width: 840px;
    height: 480px;
    background: var(--card-bg);
    box-shadow: 0 10px 30px var(--card-shadow);
    overflow: hidden;
  }
  .card--front { top: 90px; }
  .card--back { top: 630px; }

  /* Brand name lockup */
  .brand {
    position: absolute;
    display: flex;
    align-items: center;
    gap: 14px;
    color: var(--brand-blue);
    font-family: "Open Sans", sans-serif;
    font-weight: 700;
    text-transform: uppercase;
    line-height: 1;
    white-space: nowrap;
  }
  .brand__dot {
    flex: none;
    border-radius: 50%;
    background: var(--brand-blue);
  }
  .card--front .brand {
    left: 70px;
    bottom: 90px;
    font-size: 26px;
  }
  .card--front .brand__dot { width: 22px; height: 22px; }

  /* Contact block */
  .contact {
    position: absolute;
    top: 68px;
    right: 56px;
    text-align: right;
  }
  .contact__name {
    font-family: "PT Serif", serif;
    font-size: 40px;
    color: var(--brand-blue);
    font-weight: 400;
    margin-right: 44px;
    margin-bottom: 10px;
  }
  .contact__list { list-style: none; }
  .contact__item {
    display: flex;
    justify-content: flex-end;
    align-items: center;
    gap: 16px;
    height: 36px;
    font-family: "Open Sans", sans-serif;
    font-size: 21px;
    color: var(--text-dark);
    white-space: nowrap;
  }
  .contact__icon {
    width: 22px;
    height: 22px;
    flex: none;
  }

  /* Back side */
  .card--back .brand {
    left: 170px;
    top: 170px;
    font-size: 38px;
  }
  .card--back .brand__dot { width: 30px; height: 30px; }
  .slogan {
    position: absolute;
    left: 170px;
    top: 250px;
    font-family: "PT Serif", serif;
    font-style: italic;
    font-size: 26px;
    color: var(--text-dark);
    white-space: nowrap;
  }
</style>
</head>
<body>
<main class="sheet">

  <section class="card card--front" aria-label="Business card front">
    <div class="brand">
      <span class="brand__dot"></span>
      <span class="brand__name">Brindel Clear Springs</span>
    </div>

    <div class="contact">
      <h1 class="contact__name">Marla Quinlan</h1>
      <ul class="contact__list">
        <li class="contact__item">
          <span>0739184520</span>
          <svg class="contact__icon" viewBox="0 0 22 22" aria-hidden="true">
            <rect width="22" height="22" fill="var(--brand-blue)"/>
            <path d="M7 5 l2.5 0 l1 3.5 l-1.6 1.2 a8 8 0 0 0 3.4 3.4 l1.2 -1.6 l3.5 1 l0 2.5 a1.5 1.5 0 0 1 -1.5 1.5 A10 10 0 0 1 5.5 6.5 A1.5 1.5 0 0 1 7 5z" fill="#fff"/>
          </svg>
        </li>
        <li class="contact__item">
          <span>hello@brindelwater.com</span>
          <svg class="contact__icon" viewBox="0 0 22 22" aria-hidden="true">
            <rect width="22" height="22" fill="var(--brand-blue)"/>
            <rect x="5" y="7" width="12" height="8.5" fill="none" stroke="#fff" stroke-width="1.4"/>
            <path d="M5 7 l6 5 l6 -5" fill="none" stroke="#fff" stroke-width="1.4"/>
          </svg>
        </li>
        <li class="contact__item">
          <span>www.brindelclearsprings.com</span>
          <svg class="contact__icon" viewBox="0 0 22 22" aria-hidden="true">
            <rect width="22" height="22" fill="var(--brand-blue)"/>
            <circle cx="11" cy="11" r="6" fill="none" stroke="#fff" stroke-width="1.4"/>
            <ellipse cx="11" cy="11" rx="2.6" ry="6" fill="none" stroke="#fff" stroke-width="1.2"/>
            <line x1="5" y1="11" x2="17" y2="11" stroke="#fff" stroke-width="1.2"/>
          </svg>
        </li>
        <li class="contact__item">
          <span>1938 Harlow Road Fenwick TX 75412</span>
          <svg class="contact__icon" viewBox="0 0 22 22" aria-hidden="true">
            <rect width="22" height="22" fill="var(--brand-blue)"/>
            <path d="M11 18 C7 13 6.5 11 6.5 9.5 a4.5 4.5 0 0 1 9 0 C15.5 11 15 13 11 18z" fill="#fff"/>
            <circle cx="11" cy="9.5" r="1.7" fill="var(--brand-blue)"/>
          </svg>
        </li>
      </ul>
    </div>
  </section>

  <section class="card card--back" aria-label="Business card back">
    <div class="brand">
      <span class="brand__dot"></span>
      <span class="brand__name">Brindel Clear Springs</span>
    </div>
    <p class="slogan">“Clear from the very first sip”</p>
  </section>

</main>
</body>
</html>
```